Website design for Harbor Bolts. ( Lock company)

Harbor Bolts is a New York Based Company that manufactures a variety of high quality Locks which sell worldwide.

Our website: We need a 'face' on the Internet , a website that tells you who we are and what we do - 'An Identity'.

it is not an eCommerce website . the website is to show customers and potential distributers who we are and what we manufacture ( so they come away with a great impression of our company and our products) see www.quarrymillwheel.com

First glance impression: We are Professional; are locks are strong,and reliable. and we are ready to compete with other major Lock companies

Content: for starters the site will contain general information and background about our company (our story), were to buy our products, contact information, and display images of our Locks (and of course all the classic links including to all the legal and technical information). as time goes on we will add more features to the website i.e. Products, Videos blogs etc.

although at first there will not be that much content on the website - it should not look empty (it should be simple and clear but not empty) it should look and feel like a full fledged professional website (not a template)

Inspiration: here are a few sites which have the feel we are looking for:

General tone - quarrymillwheel.com bantrell.com (black is good - But not a must )

Simplicity, clarity - coolvantix.com hearthmate.com

the widescreen Image look - http://www.layoutgarden.com/demo/81952.html

we are considering perhaps having wide HQ images of Lion(s) in the background (but without the felling that it is a zoo or safari website) - it is not a must, its just an idea .

perhaps (if you find it looks good ) use a bit of that metal or chrome look to give it it a strong smooth feel (however it should not look like a dark prison)

We do not currently have a Logo ( if you feel you can design one that fits the above company description - we would love to see if it can work for us) We can talk about additional funds for the logo during this project.

Our working slogan is : Harbor Bolts - "Keeper of the Gate"

for your convenience we have attached a few images of the type of locks we sell

We are looking to collaborate with you throughout the project. We have ideas and visions we want implemented and we will help you along the way. So we can create the perfect website.

Thank you.

```html
<!DOCTYPE html>
<html lang="en">
<head>
<meta charset="utf-8">
<title>Harbor Bolts – Keeper of the Gate</title>
<link rel="stylesheet" href="https://fonts.googleapis.com/css2?family=Titillium+Web:wght@300;400;600;700&family=Open+Sans:wght@400;600&display=swap">
<style>
  :root{
    --page-bg:#1d1d20;
    --panel-bg:#0c0c0e;
    --panel-edge:#26262a;
    --red:#a3151a;
    --red-dark:#7a0c10;
    --red-text:#9a1418;
    --white:#ffffff;
    --text-dark:#333335;
    --text-muted:#8c8c92;
    --nav-top:#3a3a3e;
    --nav-bottom:#1f1f22;
    --card-top:#2a2a2e;
    --card-bottom:#0e0e10;
    --line:#2e2e32;
  }
  *{box-sizing:border-box;margin:0;padding:0}
  html,body{width:858px;height:1200px;overflow:hidden}
  body{
    background:var(--page-bg);
    font-family:"Open Sans",Arial,sans-serif;
    color:var(--white);
    position:relative;
  }
  .site{
    position:absolute;left:32px;top:36px;width:794px;height:1138px;
    background:var(--panel-bg);
    box-shadow:0 0 30px rgba(0,0,0,.6);
  }
  .hero-photo{
    position:absolute;left:0;top:0;width:794px;height:426px;
    background:
      radial-gradient(ellipse 260px 150px at 50% 22%, rgba(40,55,30,.9), transparent 70%),
      linear-gradient(180deg,#3d5a86 0%,#6f7f8e 30%,#8a6a45 55%,#6b3f1e 75%,#1a120c 100%);
  }
  .hero-padlocks{
    position:absolute;left:56px;top:135px;width:270px;height:295px;
    border-radius:50% 50% 14px 14px / 30% 30% 14px 14px;
    background:linear-gradient(180deg,#d8dde2 0%,#9aa3ab 45%,#6c7580 70%,#1e2a7a 86%,#16206a 100%);
    opacity:.9;
  }
  .logo{
    position:absolute;left:33px;top:18px;
    font-family:"Titillium Web",sans-serif;font-weight:300;font-size:32px;
    color:var(--white);letter-spacing:.2px;
  }
  .utility-links{
    position:absolute;right:33px;top:10px;
    font-size:8px;color:#e6e6e6;
  }
  .utility-links span{margin:0 3px;color:#aaa}
  .main-nav{
    position:absolute;left:33px;top:62px;width:727px;height:34px;
    background:linear-gradient(180deg,var(--nav-top),var(--nav-bottom));
    border-radius:2px;display:flex;align-items:center;
    box-shadow:0 2px 6px rgba(0,0,0,.5);
  }
  .nav-home{
    width:63px;height:34px;background:linear-gradient(180deg,#c01c22,var(--red-dark));
    display:flex;align-items:center;justify-content:center;border-radius:2px 0 0 2px;
  }
  .nav-links{display:flex;list-style:none;margin-left:27px}
  .nav-links li{
    font-family:"Titillium Web",sans-serif;font-weight:600;font-size:13px;
    margin-right:26px;color:#eee;
  }
  .hero-copy{position:absolute;left:305px;top:186px;width:360px}
  .hero-kicker{font-family:"Titillium Web",sans-serif;font-weight:400;font-size:25px;line-height:26px}
  .hero-title{font-family:"Titillium Web",sans-serif;font-weight:700;font-size:31px;line-height:36px}
  .hero-text{font-size:13px;line-height:16px;margin-top:6px;text-shadow:0 1px 2px rgba(0,0,0,.6)}
  .btn-red{
    display:flex;align-items:center;justify-content:center;
    background:linear-gradient(180deg,#c41d23,var(--red-dark));
    color:var(--white);font-family:"Titillium Web",sans-serif;font-weight:600;
    border-radius:2px;box-shadow:0 2px 4px rgba(0,0,0,.5);
  }
  .hero-btn{width:156px;height:29px;font-size:13px;margin-top:12px}

  .welcome{
    position:absolute;left:33px;top:426px;width:480px;height:258px;background:var(--white);
    color:var(--text-dark);
  }
  .welcome-title{
    position:absolute;left:26px;top:22px;font-family:"Titillium Web",sans-serif;
    font-weight:300;font-size:20px;color:#222;
  }
  .welcome-title strong{font-weight:600;color:var(--red-text)}
  .welcome-body{position:absolute;left:26px;top:60px;width:420px;font-size:10px;line-height:14.4px;color:#444}
  .welcome-body p+p{margin-top:14px}
  .newsletter{
    position:absolute;left:26px;top:220px;width:428px;border-top:1px solid #ccc;padding-top:6px;
    display:flex;align-items:center;
  }
  .newsletter-label{font-family:"Titillium Web",sans-serif;font-size:13px;color:#222;width:148px}
  .newsletter-label em{font-style:normal;color:var(--red-text)}
  .newsletter-input{
    width:218px;height:26px;border:1px solid #bbb;font-size:10px;color:#999;
    display:flex;align-items:center;padding-left:8px;
  }
  .newsletter-submit{
    width:62px;height:26px;background:#3b3b3f;color:#fff;font-size:11px;font-weight:600;
    display:flex;align-items:center;justify-content:center;
  }
  .lock-feature{
    position:absolute;left:513px;top:426px;width:247px;height:258px;
    background:linear-gradient(180deg,#2a2a2e,#111113);
  }
  .lock-feature-image{
    position:absolute;left:68px;top:-32px;width:122px;height:232px;
    border-radius:40% 40% 10px 10px / 22% 22% 10px 10px;
    background:linear-gradient(180deg,#d4d8dc 0%,#8a9096 30%,#1a1a1c 45%,#0a0a0b 100%);
  }
  .callout{position:absolute;font-size:8px;color:#ddd;line-height:9px;text-align:center}
  .callout-lines{position:absolute;left:0;top:0}
  .lock-feature-btn{position:absolute;left:0;bottom:0;width:247px;height:37px;font-size:14px;font-weight:400;border-radius:0}
  .lock-feature-btn strong{font-weight:700;margin-left:4px}

  .featured-heading{
    position:absolute;left:33px;top:724px;width:727px;height:40px;
    border-top:1px solid var(--line);border-bottom:1px solid var(--line);
    display:flex;align-items:center;justify-content:center;
    font-family:"Titillium Web",sans-serif;font-weight:600;font-size:19px;
  }
  .product-card{
    position:absolute;top:802px;width:162px;height:223px;
    background:linear-gradient(180deg,var(--card-top),var(--card-bottom) 70%);
    text-align:center;
  }
  .product-image{
    position:absolute;left:36px;top:-10px;width:90px;height:106px;
    border-radius:45% 45% 8px 8px / 35% 35% 8px 8px;
    background:linear-gradient(180deg,#dadfe3 0%,#9aa2aa 45%,#7a838c 70%,#1e2a80 85%,#141c5e 100%);
  }
  .product-name{position:absolute;left:0;top:145px;width:100%;font-family:"Titillium Web",sans-serif;font-weight:600;font-size:13px}
  .product-text{position:absolute;left:14px;top:172px;width:134px;font-size:8.5px;line-height:12px;color:var(--text-muted)}
  .product-bar{
    position:absolute;left:0;bottom:-36px;width:162px;height:23px;background:#1e1e21;
    display:flex;align-items:center;
  }
  .product-bar span{flex:1;font-size:10px;font-weight:600;color:#eee;padding-left:10px}
  .product-arrow{width:26px;height:23px;background:var(--red);display:flex;align-items:center;justify-content:center}

  .site-footer{
    position:absolute;left:0;top:1056px;width:794px;height:82px;background:#0d0d0f;
    border-top:1px solid #1e1e22;
  }
  .footer-links{position:absolute;left:33px;top:32px;font-size:9px;color:#8a8a90}
  .footer-links span{margin:0 3px}
  .copyright{position:absolute;right:33px;top:32px;font-size:9px;color:#8a8a90}
</style>
</head>
<body>
<div class="site">
  <div class="hero-photo" role="img" aria-label="Wide savanna landscape at dusk with an acacia tree and a resting lion"></div>
  <div class="hero-padlocks" role="img" aria-label="Two laminated steel padlocks with a key"></div>

  <header>
    <div class="logo">Harbor Bolts</div>
    <div class="utility-links">Warranty Info<span>|</span>Legal<span>|</span>Privacy Policy<span>|</span>Sitemap</div>
    <nav class="main-nav">
      <div class="nav-home">
        <svg width="14" height="12" viewBox="0 0 14 12"><path d="M7 0 14 6h-2v6H9V8H5v4H2V6H0z" fill="#fff"/></svg>
      </div>
      <ul class="nav-links">
        <li>Our Products</li><li>Where to Buy</li><li>About Us</li><li>Gallery</li><li>Blog</li><li>Contact Us</li>
      </ul>
    </nav>
  </header>

  <section class="hero-copy">
    <div class="hero-kicker">Harbor Bolts</div>
    <h1 class="hero-title">Keeper of the Gate</h1>
    <p class="hero-text">Lorem ipsum dolor sit amet, consectetur adipiscing elit. Nullam consequat lacus eu sodales gravida. Maecenas a molestie tortor.</p>
    <div class="btn-red hero-btn">learn more</div>
  </section>

  <section class="welcome">
    <h2 class="welcome-title">Welcome to <strong>Harbor Bolts</strong></h2>
    <div class="welcome-body">
      <p>Lorem ipsum dolor sit amet, consectetur adipiscing elit. Aliquam tellus mi, porttitor nec tempus vitae, placerat eget metus. Suspendisse tincidunt dolor eu sem tempus malesuada. Aliquam feugiat facilisis eros rhoncus volutpat.</p>
      <p>Nulla adipiscing iaculis tortor, ut laoreet felis pharetra a. Mauris quis rhoncus arcu. Nam commodo eget dui eget sollicitudin. Cras magna diam, scelerisque vitae justo id, ornare semper arcu. Nulla luctus mollis velit in lobortis.</p>
    </div>
    <div class="newsletter">
      <div class="newsletter-label">Sign Up for <em>Newsletter</em></div>
      <div class="newsletter-input">Your email address</div>
      <div class="newsletter-submit">submit</div>
    </div>
  </section>

  <aside class="lock-feature">
    <div class="lock-feature-image" role="img" aria-label="Black combination key-safe lock with chrome shackle"></div>
    <svg class="callout-lines" width="247" height="200" viewBox="0 0 247 200">
      <path d="M48 84V36h30M200 78V110h-22" stroke="#aaa" stroke-width="1" fill="none"/>
    </svg>
    <div class="callout" style="left:180px;top:82px">code protect</div>
    <div class="callout" style="left:18px;top:156px">chrome-plated<br>steel</div>
    <div class="btn-red lock-feature-btn">Learn more about our<strong>locks</strong>
      <svg width="14" height="10" viewBox="0 0 14 10" style="margin-left:10px"><path d="M1 1l4 4-4 4M7 1l4 4-4 4" stroke="#fff" stroke-width="2" fill="none"/></svg>
    </div>
  </aside>

  <h2 class="featured-heading">Our Featured Products</h2>

  <article class="product-card" style="left:33px">
    <div class="product-image" role="img" aria-label="Laminated steel padlock with keys"></div>
    <h3 class="product-name">Lock mode name</h3>
    <p class="product-text">Lorem ipsum dolor sit amet, consectetur adipiscing elit. Aliquam tellus mi, porttitor nec tempus</p>
    <div class="product-bar"><span>learn more</span><div class="product-arrow"><svg width="8" height="10" viewBox="0 0 8 10"><path d="M2 1l4 4-4 4" stroke="#fff" stroke-width="2" fill="none"/></svg></div></div>
  </article>
  <article class="product-card" style="left:221px">
    <div class="product-image" role="img" aria-label="Laminated steel padlock with keys"></div>
    <h3 class="product-name">Lock mode name</h3>
    <p class="product-text">Lorem ipsum dolor sit amet, consectetur adipiscing elit. Aliquam tellus mi, porttitor nec tempus</p>
    <div class="product-bar"><span>learn more</span><div class="product-arrow"><svg width="8" height="10" viewBox="0 0 8 10"><path d="M2 1l4 4-4 4" stroke="#fff" stroke-width="2" fill="none"/></svg></div></div>
  </article>
  <article class="product-card" style="left:408px">
    <div class="product-image" role="img" aria-label="Laminated steel padlock with keys"></div>
    <h3 class="product-name">Lock mode name</h3>
    <p class="product-text">Lorem ipsum dolor sit amet, consectetur adipiscing elit. Aliquam tellus mi, porttitor nec tempus</p>
    <div class="product-bar"><span>learn more</span><div class="product-arrow"><svg width="8" height="10" viewBox="0 0 8 10"><path d="M2 1l4 4-4 4" stroke="#fff" stroke-width="2" fill="none"/></svg></div></div>
  </article>
  <article class="product-card" style="left:597px">
    <div class="product-image" role="img" aria-label="Laminated steel padlock with keys"></div>
    <h3 class="product-name">Lock mode name</h3>
    <p class="product-text">Lorem ipsum dolor sit amet, consectetur adipiscing elit. Aliquam tellus mi, porttitor nec tempus</p>
    <div class="product-bar"><span>learn more</span><div class="product-arrow"><svg width="8" height="10" viewBox="0 0 8 10"><path d="M2 1l4 4-4 4" stroke="#fff" stroke-width="2" fill="none"/></svg></div></div>
  </article>

  <footer class="site-footer">
    <div class="footer-links">Our Products<span>|</span>Where to Buy<span>|</span>About Us<span>|</span>Gallery<span>|</span>Blog<span>|</span>Contact Us</div>
    <div class="copyright">Harbor Bolts ©2014 All rights reserved.</div>
  </footer>
</div>
</body>
</html>
```